Chiropractic Business card

We need a new business card for a chiropractic doctor office. I attract the sports/athletic type of patients.
my old card was an ice blue on the front with black lettering and black on the back with blue lettering. the front had my name as the main focus and the office name under it smaller and then contact info on the bottom, the back of card had my website as the center focus and our technique specialty small across the bottom. It was a simple design and would like to see what I could gain here.
I want a front and back card design
I would still want my name as the main focus of the card (Lyle Brandt, DC) the then next focus would be my website address www.brandtchiropractic.example and then maybe www.socialpage.example/brandtchiropractic smaller underneath it or whatever works with your design.
Must have
Lyle Brandt, DC
Brandt Chiropractic & Sports Center
210.555.0147
drlyle@brandtchiropractic.example
4829b Marlowe Ridge San Antonio, TX 78216
www.brandtchiropractic.example
www.socialpage.example/brandtchiropractic
(not a main focus of card but would like to have the following small on the card, these are our specailty techniques)
Applied Kinesiology - Cold Laser - Nutrition - Detox - Allergies - Dynamic Tissue Methods
(if space is a problem eliminate Detox and Allergies)
then if there is any room left over our slogan is about
- Performance Recovery and Longevity - (I would really like this on the card but space might become a problem)
I like Blues, Blacks, Silvers/grey, white but open to your design
standard type which is 2" by 3.5" with a 5mm bleed area
I don't have an offical logo but sometimes use the attached file as a pic.

```html
<!DOCTYPE html>
<html lang="en">
<head>
<meta charset="utf-8">
<title>Brandt Chiropractic – Business Card Front and Back</title>
<link rel="stylesheet" href="https://fonts.googleapis.com/css2?family=Source+Sans+3:wght@400;600;700&display=swap">
<style>
  :root {
    --page: #ffffff;
    --navy: #1d3f7d;
    --royal: #24528f;
    --teal-glow: #3fa6b9;
    --name-blue: #2f64a8;
    --text-grey: #555a60;
    --card-light: #f4f5f6;
    --band-top: #2c5c9c;
    --band-bottom: #1d3f78;
    --band-edge: #8cc3e6;
    --white: #ffffff;
  }
  * { margin: 0; padding: 0; box-sizing: border-box; }
  html, body {
    width: 978px; height: 1200px; overflow: hidden;
    background: var(--page);
    font-family: "Source Sans 3", "Helvetica Neue", Arial, sans-serif;
  }
  .sheet { position: relative; width: 978px; height: 1200px; }

  .card {
    position: absolute;
    border-radius: 22px;
    overflow: hidden;
    box-shadow: 4px 6px 10px rgba(0,0,0,0.35);
  }

  /* Front */
  .card--front {
    left: 65px; top: 78px; width: 827px; height: 471px;
    background: radial-gradient(ellipse 380px 300px at 410px 150px, var(--teal-glow) 0%, var(--royal) 55%, var(--navy) 100%);
  }
  .card--front .figure-art {
    position: absolute; left: 457px; top: 77px; width: 326px; height: 334px;
    background: radial-gradient(ellipse at 50% 40%, rgba(110,170,225,0.55) 0%, rgba(60,110,180,0.35) 45%, rgba(40,80,150,0) 75%);
  }
  .card--front .doctor-name {
    position: absolute; left: 54px; top: 248px;
    font-size: 41px; font-weight: 700; color: var(--white); letter-spacing: 0.5px;
  }
  .card--front .practice-name {
    position: absolute; left: 55px; top: 300px;
    font-size: 22px; font-weight: 400; color: #dfe8f4;
  }
  .card--front .website {
    position: absolute; left: 55px; top: 386px;
    font-size: 24px; font-weight: 600; color: var(--white);
  }

  /* Back */
  .card--back {
    left: 73px; top: 628px; width: 828px; height: 474px;
    background: linear-gradient(180deg, #ffffff 0%, var(--card-light) 100%);
  }
  .card--back .figure-art {
    position: absolute; left: 50px; top: 140px; width: 350px; height: 290px;
    background: radial-gradient(ellipse at 50% 40%, rgba(190,200,210,0.45) 0%, rgba(220,225,230,0.2) 55%, rgba(255,255,255,0) 80%);
  }
  .card--back .doctor-name {
    position: absolute; left: 66px; top: 44px;
    font-size: 40px; font-weight: 700; color: var(--name-blue); letter-spacing: 0.5px;
  }
  .card--back .practice-name {
    position: absolute; left: 67px; top: 95px;
    font-size: 21px; font-weight: 400; color: var(--name-blue);
  }
  .social {
    position: absolute; right: 65px; top: 56px;
    display: flex; align-items: center; gap: 8px;
    font-size: 20px; font-weight: 600; color: var(--navy);
  }
  .social__square { width: 18px; height: 18px; background: var(--navy); }

  .contact {
    position: absolute; right: 72px; top: 225px;
    list-style: none; text-align: right;
    font-size: 24px; color: var(--text-grey); line-height: 34px;
  }
  .contact li { display: flex; justify-content: flex-end; align-items: center; gap: 8px; }
  .contact svg { fill: var(--royal); }

  .specialty-band { position: absolute; left: 0; bottom: 0; width: 828px; height: 112px; }
  .specialties {
    position: absolute; left: 0; right: 0; bottom: 34px;
    display: flex; justify-content: center; align-items: center; gap: 12px;
    list-style: none;
    font-size: 19px; font-weight: 600; color: var(--white);
  }
  .specialties li + li::before {
    content: ""; display: inline-block; width: 5px; height: 5px; border-radius: 50%;
    background: var(--white); margin-right: 12px; vertical-align: middle;
  }
</style>
</head>
<body>
<main class="sheet">

  <section class="card card--front">
    <div class="figure-art" role="img" aria-label="Translucent blue anatomical human figure with outstretched arms"></div>
    <h1 class="doctor-name">LYLE BRANDT, DC</h1>
    <p class="practice-name">Brandt Chiropractic &amp; Sports Center</p>
    <p class="website">www.brandtchiropractic.example</p>
  </section>

  <section class="card card--back">
    <div class="figure-art" role="img" aria-label="Faint grey anatomical human figure with outstretched arms"></div>
    <h2 class="doctor-name">LYLE BRANDT, DC</h2>
    <p class="practice-name">Brandt Chiropractic &amp; Sports Center</p>

    <div class="social"><span class="social__square"></span><span>brandtchiropractic</span></div>

    <ul class="contact">
      <li>
        <svg width="14" height="22" viewBox="0 0 14 22" aria-hidden="true"><rect x="1" y="3" width="12" height="18" rx="2"/><rect x="3" y="0" width="2" height="4"/><rect x="3.5" y="6" width="7" height="5" fill="#fff"/></svg>
        <span>210.555.0147</span>
      </li>
      <li>
        <svg width="18" height="13" viewBox="0 0 18 13" aria-hidden="true"><rect width="18" height="13" rx="1.5"/><path d="M1 1.5 L9 7.5 L17 1.5" fill="none" stroke="#fff" stroke-width="1.5"/></svg>
        <span>drlyle@brandtchiropractic.example</span>
      </li>
      <li>
        <svg width="22" height="20" viewBox="0 0 22 20" aria-hidden="true"><path d="M11 0 L22 10 L19 10 L19 20 L13.5 20 L13.5 13 L8.5 13 L8.5 20 L3 20 L3 10 L0 10 Z"/></svg>
        <span>4829b Marlowe Ridge San Antonio, TX 78216</span>
      </li>
    </ul>

    <svg class="specialty-band" viewBox="0 0 828 112" preserveAspectRatio="none" aria-hidden="true">
      <defs>
        <linearGradient id="bandFill" x1="0" y1="0" x2="0" y2="1">
          <stop offset="0" stop-color="var(--band-top)"/>
          <stop offset="1" stop-color="var(--band-bottom)"/>
        </linearGradient>
      </defs>
      <path d="M0 26 Q414 -12 828 26 L828 112 L0 112 Z" fill="var(--band-edge)"/>
      <path d="M0 32 Q414 -4 828 32 L828 112 L0 112 Z" fill="url(#bandFill)"/>
    </svg>
    <ul class="specialties">
      <li>Applied Kinesiology</li>
      <li>Cold Laser</li>
      <li>Nutrition</li>
      <li>Dynamic Tissue Methods</li>
    </ul>
  </section>

</main>
</body>
</html>
```